I need a business card design for a new company that will be doing consulting work around issues of cultural competency, and diversity and inclusion. I would like the design to be crisp and clear with bold but conservative colors and incorporate shades of blue

Target Market(s)

Small businesses, schools, non-profits

Industry/Entity Type

Consulting

Font styles to use
Serif
Sans Serif

Colors
0c5ba6
6b449b
3276b5
0292cd

Requirements
Must have
• A Morrow Venture (name of company)
• Lemlem Tavish
• CEO
• lemlem@amorrowventure.com
• (215)483-2756

```html
<!DOCTYPE html>
<html lang="en">
<head>
<meta charset="utf-8">
<title>A Morrow Venture – Business Card</title>
<link rel="stylesheet" href="https://fonts.googleapis.com/css2?family=Montserrat:wght@700&family=Questrial&display=swap">
<style>
  :root {
    --backdrop: #e4e4e4;
    --card: #ffffff;
    --ink: #2b2b2b;
    --blue-deep: #2f77b5;
    --blue-bright: #0292cd;
    --violet: #6b449b;
    --violet-fade: #ffffff;
  }
  html, body {
    margin: 0;
    padding: 0;
    width: 1200px;
    height: 1199px;
    overflow: hidden;
    background: var(--backdrop);
  }
  .stage {
    width: 1200px;
    height: 1199px;
    display: flex;
    align-items: center;
    justify-content: center;
  }
  .business-card {
    display: block;
    width: 1100px;
    height: 660px;
    background: var(--card);
  }
  .band-top { fill: var(--blue-deep); }
  .band-back { fill: var(--blue-deep); }
  .band-corner { fill: var(--blue-bright); }
  .company-name {
    font-family: "Questrial", sans-serif;
    font-size: 35px;
    fill: var(--ink);
  }
  .person-name {
    font-family: "Montserrat", sans-serif;
    font-weight: 700;
    font-size: 45px;
    fill: var(--ink);
  }
  .person-title {
    font-family: "Questrial", sans-serif;
    font-size: 27px;
    fill: var(--ink);
  }
  .contact {
    font-family: "Questrial", sans-serif;
    font-size: 23px;
    fill: var(--ink);
  }
  .icon-fill { fill: var(--ink); }
  .icon-line { fill: none; stroke: var(--ink); stroke-width: 1.2; }
</style>
</head>
<body>
<main class="stage">
  <svg class="business-card" viewBox="0 0 700 420" xmlns="http://www.w3.org/2000/svg">
    <defs>
      <linearGradient id="contact-band-gradient" x1="0" y1="0" x2="1" y2="0">
        <stop offset="0" stop-color="var(--violet)"/>
        <stop offset="1" stop-color="var(--violet-fade)"/>
      </linearGradient>
    </defs>

    <rect class="card-face" width="700" height="420" fill="var(--card)"/>

    <polygon class="band-top" points="0,0 246,0 206,74 0,74"/>
    <polygon class="band-back" points="286,270 700,270 700,420 200,420"/>
    <polygon class="band-corner" points="0,323 150,323 97,420 0,420"/>
    <polygon class="band-contact" points="212,293 607,293 538,420 142,420" fill="url(#contact-band-gradient)"/>

    <text class="company-name" x="350" y="126" text-anchor="middle">A Morrow Venture</text>
    <text class="person-name" x="350" y="199" text-anchor="middle">Lemlem Tavish</text>
    <text class="person-title" x="350" y="242" text-anchor="middle">CEO</text>

    <g class="contact-phone">
      <path class="icon-fill" transform="translate(394,333) scale(0.9)"
        d="M4 1 L8 1 L10 6 L7.5 8 C9 11 11 13 14 14.5 L16 12 L21 14 L21 18 C21 19.5 19.5 21 18 21 C9 20 2 13 1 4 C1 2.5 2.5 1 4 1 Z"/>
      <text class="contact" x="570" y="350" text-anchor="end">(215)483-2756</text>
    </g>

    <g class="contact-email">
      <rect class="icon-line" x="192" y="366" width="14" height="10"/>
      <polyline class="icon-line" points="192,366 199,372 206,366"/>
      <text class="contact" x="547" y="377" text-anchor="end">lemlem@amorrowventure.com</text>
    </g>
  </svg>
</main>
</body>
</html>
```